We need a new design for our construction website

We need a new website for our wordpress site kerrowmade.co.nz

It needs to be only a few pages but sleek in design and responsive, beautifully showcasing our images and video. Currently we have
1. home
2. about us
3. contact
We need either a front page that is designed much better to showcase more content, or potentially a projects page which has images from our builds. We don't have a lot of content so the content we do have needs to be maximised by image, rather than project.

Target Market(s)

High end residential construction and renovation projects, people wanting to build a nice home, clients based in Mount Maunganui, Tauranga.

Coding

Font styles to use
Sans Serif

Colors

Designer to choose only greyscale colors for use in the design.

Requirements
Must have
• A sleek design, architectural

```html
<!DOCTYPE html>
<html lang="en">
<head>
<meta charset="utf-8">
<title>Kerrowmade — Sustainable Construction Solutions</title>
<link rel="stylesheet" href="https://fonts.googleapis.com/css2?family=Jost:wght@300;400&display=swap">
<style>
:root{
  --bg:#e9e9e9;
  --panel:#c9c9c9;
  --white:#ffffff;
  --ink:#1c1c1c;
  --text:#4a4a4a;
  --muted:#6b6b6b;
  --tile:#3c3c3c;
  --highlight:#8a8a8a;
}
*{margin:0;padding:0;box-sizing:border-box}
html,body{width:1200px;height:3192px;overflow:hidden;background:var(--bg)}
body{position:relative;font-family:"Jost",Arial,sans-serif;font-weight:300;color:var(--text)}
.abs{position:absolute}
a{color:inherit;text-decoration:none}

/* header */
.brand{left:200px;top:18px;display:flex;align-items:center;gap:10px;font-weight:300;font-size:17px;letter-spacing:6px;color:var(--muted)}
.brand-mark{width:26px;height:26px;border:1.5px solid var(--muted)}
.main-nav{left:628px;top:20px;display:flex;gap:17px;font-size:16px;font-weight:300;color:var(--text)}

.tower-photo{left:819px;top:56px;width:370px;height:526px;background:linear-gradient(180deg,#d6d6d6 0%,#bdbdbd 40%,#9a9a9a 60%,#c4c4c4 100%);clip-path:polygon(0 12%,10% 8%,70% 0,100% 12%,100% 100%,0 100%)}

.hero-kicker{left:304px;top:188px;font-size:23px;font-weight:300;color:var(--ink)}
.hero-title{left:302px;top:212px;font-size:62px;line-height:74px;font-weight:400;color:var(--ink);letter-spacing:-0.5px}
.hero-sub{left:304px;top:280px;font-size:23px;font-weight:300;color:var(--ink)}
.slider-controls{left:304px;top:337px;display:flex}
.slider-controls span{width:41px;height:44px;border:1.3px solid var(--ink);display:flex;align-items:center;justify-content:center}
.slider-controls span+span{border-left:none}

/* projects */
.projects-tab{left:304px;top:458px;width:282px;height:132px;background:var(--panel)}
.projects-tab-label{left:338px;top:488px;font-size:15px;font-weight:400;color:var(--ink);letter-spacing:-0.2px}
.projects-tab-rule{left:337px;top:532px;width:105px;height:3px;background:var(--ink)}
.projects-panel{left:200px;top:589px;width:1000px;height:702px;background:var(--panel)}
.project-grid{left:247px;top:671px;display:grid;grid-template-columns:repeat(3,207px);column-gap:54px;row-gap:38px}
.project-card{text-align:center}
.project-photo{width:207px;height:207px}
.project-name{margin-top:10px;font-size:16px;font-weight:400;color:var(--ink);letter-spacing:0.4px}
.p1{background:linear-gradient(135deg,#3c3c3c 0 30%,#6e6e6e 30% 55%,#9a9a9a 55% 100%)}
.p2{background:radial-gradient(circle at 60% 60%,#f1f1f1 0 40%,#c6c6c6 55%,#3c3c3c 70%)}
.p3{background:linear-gradient(135deg,#3c3c3c 0 48%,#9a9a9a 50%,#d2d2d2 100%)}
.p4{background:linear-gradient(90deg,#3c3c3c 0 8%,#acacac 10% 90%,#3c3c3c 92%)}
.p5{background:linear-gradient(160deg,#3c3c3c 0 35%,#e7e7e7 40%,#a0a0a0 100%)}
.p6{background:radial-gradient(circle at 95% 100%,#f4f4f4 0 60%,#dcdcdc 70%,#3c3c3c 72%)}

/* history */
.history-strip{left:1091px;top:1291px;width:109px;height:621px;background:var(--panel)}
.section-label{font-size:20px;letter-spacing:9px;color:var(--muted);font-weight:300}
.history-label{left:200px;top:1458px}
.history-lead{left:600px;top:1458px;width:410px;font-size:24px;font-weight:300;line-height:35px;color:var(--text)}
.history-body{left:600px;top:1604px;width:410px;font-size:17px;font-weight:300;line-height:26.6px;color:var(--text)}
.drawing-photo{left:0;top:1612px;width:440px;height:378px;background:linear-gradient(120deg,#d5d5d5 0%,#f2f2f2 45%,#e4e4e4 70%,#b9b9b9 100%)}

/* services */
.services-panel{left:280px;top:2004px;width:920px;height:490px;background:var(--panel)}
.services-label{left:248px;top:2188px;transform:translate(-50%,-50%) rotate(-90deg);white-space:nowrap}
.service{width:290px}
.service h3{font-size:21px;font-weight:300;color:var(--text);margin-bottom:12px}
.service p{font-size:13px;font-weight:300;line-height:22px;color:var(--text)}
.s1{left:351px;top:2028px}
.s2{left:698px;top:2028px}
.s3{left:351px;top:2272px}
.s4{left:698px;top:2272px;width:305px}
.more-tab{left:280px;top:2494px;width:267px;height:70px;background:var(--panel)}
.more-link{left:334px;top:2508px;font-size:24px;font-weight:400;color:var(--ink);text-decoration:underline;text-underline-offset:3px}

.facade-photo{left:0;top:2560px;width:1179px;height:632px;background:linear-gradient(90deg,#2a2a2a 0%,#8a8a8a 18%,#363636 35%,#9a9a9a 55%,#2c2c2c 75%,#1b1b1b 100%);clip-path:polygon(0 28%,12% 16%,20% 12%,43% 2%,52% 18%,62% 30%,75% 32%,84% 26%,92% 50%,100% 100%,0 100%)}

/* footer */
.site-footer{left:281px;top:2962px;width:764px;height:230px;background:var(--panel)}
.footer-brand{left:332px;top:3010px}
.socials{left:601px;top:3014px;display:flex;gap:17px}
.socials span{width:27px;height:27px;background:var(--muted);border-radius:3px}
.footer-nav{left:375px;top:3056px;font-size:16px;font-weight:300;line-height:31px;color:var(--ink)}
.footer-contact{left:601px;top:3056px;font-size:16px;font-weight:300;line-height:31px;color:var(--ink)}
.footer-contact .hl{color:var(--highlight)}
</style>
</head>
<body>

<header>
  <div class="abs brand"><span class="brand-mark"></span>KERROWMADE</div>
  <nav class="abs main-nav"><a>Home</a><a>Projects</a><a>Our History</a><a>Services</a><a>Contacts</a></nav>
</header>

<div class="abs tower-photo" role="img" aria-label="Photo of a tall modern office tower"></div>

<section class="hero">
  <p class="abs hero-kicker">We Specialize In Sustainable</p>
  <h1 class="abs hero-title">Construction</h1>
  <p class="abs hero-sub">Solutions</p>
  <div class="abs slider-controls">
    <span><svg width="10" height="16" viewBox="0 0 10 16"><path d="M8 1 1 8l7 7" fill="none" stroke="#1c1c1c" stroke-width="1.4"/></svg></span>
    <span><svg width="10" height="16" viewBox="0 0 10 16"><path d="M2 1l7 7-7 7" fill="none" stroke="#1c1c1c" stroke-width="1.4"/></svg></span>
  </div>
</section>

<section class="projects">
  <div class="abs projects-tab"></div>
  <svg class="abs" style="left:586px;top:529px" width="53" height="53" viewBox="0 0 53 53"><polygon points="0,0 53,0 53,53" fill="#fff"/><polygon points="0,0 53,53 0,53" fill="#c9c9c9"/></svg>
  <p class="abs projects-tab-label">SEE OUR RECENT PROJECTS</p>
  <div class="abs projects-tab-rule"></div>
  <div class="abs projects-panel"></div>
  <svg class="abs" style="left:200px;top:1219px" width="71" height="72" viewBox="0 0 71 72"><polygon points="0,0 71,72 0,72" fill="#e9e9e9"/><polygon points="0,0 71,0 71,72" fill="#fff"/></svg>
  <div class="abs project-grid">
    <div class="project-card"><div class="project-photo p1" role="img" aria-label="Commercial building facade"></div><p class="project-name">COMMERCIAL</p></div>
    <div class="project-card"><div class="project-photo p2" role="img" aria-label="Curving white cultural centre"></div><p class="project-name">CULTURAL / LIFESTYLE</p></div>
    <div class="project-card"><div class="project-photo p3" role="img" aria-label="Angular educational building corner"></div><p class="project-name">EDUCATIONAL</p></div>
    <div class="project-card"><div class="project-photo p4" role="img" aria-label="Rounded glass healthcare tower"></div><p class="project-name">HEALTHCARE</p></div>
    <div class="project-card"><div class="project-photo p5" role="img" aria-label="Stacked white government building"></div><p class="project-name">GOVERNMENT</p></div>
    <div class="project-card"><div class="project-photo p6" role="img" aria-label="Curved white industrial facade"></div><p class="project-name">INDUSTRIAL</p></div>
  </div>
</section>

<section class="history">
  <div class="abs history-strip"></div>
  <h2 class="abs section-label history-label">OUR HISTORY</h2>
  <p class="abs history-lead">Our construction company has been founded 10 years ago, at the very peak of the building frenzy in the US</p>
  <p class="abs history-body">Since then we've built hundreds of commercial, government and private buildings and facilities. It may not sound like a lot, but if you estimate the manpower, working hours, materials, planning and correlating that were all involved in completing each separate project, then our productivity is immense!</p>
  <div class="abs drawing-photo" role="img" aria-label="Photo of a hand sketching architectural plans with a pen"></div>
  <svg class="abs" style="left:350px;top:1612px" width="90" height="82" viewBox="0 0 90 82"><polygon points="0,0 90,0 90,82" fill="#e9e9e9"/><polygon points="0,0 90,82 0,82" fill="#fff"/></svg>
</section>

<section class="services">
  <div class="abs services-panel"></div>
  <h2 class="abs section-label services-label">OUR SERVICES</h2>
  <div class="abs service s1"><h3>Design and Build</h3><p>The Design and Build process streamlines your home construction project ensuring your architect or designer and builder are on the same page from day one meaning you get the dream home you've always wanted.</p></div>
  <div class="abs service s2"><h3>Renovations &amp; Additions</h3><p>Improving the layout and functionality of your home doesn't mean having to build from scratch, renovations and additions can modernise your home, improve things like energy efficiency and the way that your building "performs."</p></div>
  <div class="abs service s3"><h3>Project Management</h3><p>We specialise in managing your entire build project. From liaising with your designer, engineers, advising you on the best building materials, sourcing trustworthy subcontractors and scheduling and managing the roll-out of each build stage. We are experienced and have a reputation for on-time, on-budget builds.</p></div>
  <div class="abs service s4"><h3>Build Smarter</h3><p>We are passionate about building smarter, even better than the building code. When it comes to energy efficiency, a warm and healthy home performs with true efficiency. What do we mean? Comfort, thermally-broken, well designed and the best quality materials to match your project budget.</p></div>
  <div class="abs more-tab"></div>
  <svg class="abs" style="left:547px;top:2494px" width="70" height="70" viewBox="0 0 70 70"><polygon points="0,0 70,0 0,70" fill="#fff"/></svg>
  <a class="abs more-link">Find Out More</a>
</section>

<div class="abs facade-photo" role="img" aria-label="Photo of a row of tall metal facade fins"></div>

<footer>
  <div class="abs site-footer"></div>
  <div class="abs brand footer-brand"><span class="brand-mark"></span>KERROWMADE</div>
  <div class="abs socials" aria-label="Social links"><span></span><span></span><span></span></div>
  <nav class="abs footer-nav"><p>Home</p><p>Projects</p><p>Our History</p><p>Services</p></nav>
  <div class="abs footer-contact">
    <p>Address: Unit 4 18 Harbour Rd, Mount Maunganui 3116</p>
    <p>Phone: <span class="hl">(800) 555-0172</span></p>
    <p>E-mail: <span class="hl">hello@kerrowmade.co.nz</span></p>
    <p>We are open Mn-Fr: 10 am-8 pm</p>
  </div>
</footer>

</body>
</html>
```